NoraB Designs

To have a blog that is interactive and shows products that I produce, with the ability to direct people to ClipVantor and Brimo

I not only do papercrafting but also do sublimition on T-shirts, and other items. I do the designs for all of them. So I need to have pages to decifer these.

I have logo's done. and can provide them.

Target Market(s)

Handmade cards, home projects, sublimiated items (shirts, cups, dog items)

Industry/Entity Type

Gift Shop

Number of Pages Required

4 page

Font styles to use
Serif

Requirements
Must have
• easy to operate for everyone, with good directions, connections to Brimo shop and ClipVantor, along with shopping from suppliers
Nice to have
• I would like the site to be one that clean but happy feeling, one that people will remember and return to. If someone is looking at something specific, maybe a new page to open
Should not have
• a confusing site.

```html
<!DOCTYPE html>
<html lang="en">
<head>
<meta charset="utf-8">
<title>NoraB Designs</title>
<link href="https://fonts.googleapis.com/css2?family=Poppins:wght@500;600;700&family=Lato:wght@400;700&display=swap" rel="stylesheet">
<style>
:root{
  --purple:#4a2c8c;
  --purple-dark:#3f2479;
  --ink:#1f1f24;
  --muted:#3b3b44;
  --line:#e4e2e8;
  --about-bg:#f4f1f2;
  --white:#ffffff;
  --gold:#c99a3b;
}
*{box-sizing:border-box;margin:0;padding:0}
html,body{width:1200px;height:3275px;overflow:hidden;background:var(--white)}
body{position:relative;font-family:'Lato',sans-serif;color:var(--ink)}
.abs{position:absolute}
.heading{font-family:'Poppins',sans-serif;font-weight:700;color:var(--ink);text-transform:uppercase}
.rule{width:30px;height:3px;background:var(--purple);margin:12px auto 0}
.btn{display:inline-block;background:var(--purple);color:var(--white);font-family:'Poppins',sans-serif;font-weight:600;text-transform:uppercase}

/* header */
.site-header{left:0;top:0;width:1200px;height:132px;background:var(--white)}
.brand{display:flex;align-items:center;gap:10px}
.brand-dot{border-radius:50%;border:2px solid var(--gold);flex:none}
.brand-name{font-family:'Poppins',sans-serif;font-weight:600;color:var(--purple)}
.header-brand{left:128px;top:34px}
.header-brand .brand-dot{width:56px;height:56px}
.header-brand .brand-name{font-size:20px}
.search{left:549px;top:28px;width:237px;height:34px;border:1px solid #9a9aa2;display:flex;align-items:center;justify-content:space-between;padding:0 12px;font-size:11px;color:#333}
.follow{left:820px;top:30px;display:flex;align-items:center;gap:10px;font-family:'Poppins',sans-serif;font-size:11px;font-weight:500;color:var(--ink)}
.follow .nets{color:var(--purple)}
.main-nav{left:418px;top:88px;display:flex;gap:0;font-family:'Poppins',sans-serif;font-size:15px;font-weight:500;text-transform:uppercase}
.main-nav a{color:var(--ink);text-decoration:none;margin-right:44px}
.main-nav a.active{color:var(--purple);font-weight:600}
.main-nav a:last-child{margin-right:0}

/* hero */
.hero{left:0;top:132px;width:1200px;height:574px;background:linear-gradient(100deg,#7d8a6a 0%,#b9c7c0 22%,#d6e3ea 40%,#9fc6cf 52%,#e3d6de 66%,#d59ab2 80%,#7fb7c4 100%)}
.hero-shade{left:0;top:132px;width:1200px;height:574px;background:linear-gradient(180deg,rgba(20,20,26,.15),rgba(20,20,26,.35))}
.hero-arrow{top:400px;width:36px;height:36px;background:var(--purple);display:flex;align-items:center;justify-content:center}
.hero-panel{left:349px;top:465px;width:502px;height:169px;background:rgba(40,38,44,.62);text-align:center;color:var(--white);padding-top:28px}
.hero-title{font-family:'Poppins',sans-serif;font-weight:700;font-size:31px;text-transform:uppercase;line-height:1}
.hero-text{font-size:18px;line-height:23px;margin:18px auto 0;width:400px}
.hero-btn{left:478px;top:632px;width:243px;height:45px;line-height:41px;text-align:center;font-size:15px;border:2px solid var(--white)}

/* popular */
.wash{border-radius:50%;filter:blur(30px)}
.popular-title{left:0;top:750px;width:1200px;text-align:center;font-size:21px}
.post-list{left:116px;top:839px;display:flex;gap:21px}
.post-card{width:226px;height:441px;border:1px solid var(--line);background:var(--white);padding:14px 16px 0}
.post-thumb{width:192px;height:254px}
.post-title{font-family:'Poppins',sans-serif;font-weight:600;font-size:12px;line-height:17px;text-transform:uppercase;margin-top:20px;min-height:34px}
.post-text{font-size:11.5px;line-height:16px;color:var(--muted);margin-top:8px;height:56px}
.post-btn{font-size:10px;padding:5px 8px;margin-top:12px}

/* about */
.about{left:0;top:1345px;width:1200px;height:445px;background:var(--about-bg)}
.about-brand{left:182px;top:1388px;width:360px;height:360px;flex-direction:column;justify-content:center}
.about-brand .brand-dot{width:210px;height:210px;display:flex;align-items:center;justify-content:center}
.about-brand .brand-name{font-size:30px}
.about-copy{left:652px;top:1397px;width:410px}
.about-copy .heading{font-size:21px}
.about-copy .rule{margin:12px 0 0;width:72px}
.about-copy p{font-size:15.5px;line-height:25.6px;color:var(--muted);margin-top:28px}
.about-btn{font-size:10px;padding:8px 16px;margin-top:32px}

/* categories */
.cat-title{left:0;top:1852px;width:1200px;text-align:center;font-size:21px}
.cat-grid{left:132px;top:1941px;display:grid;grid-template-columns:repeat(4,218px);column-gap:22px;row-gap:30px}
.cat-card{height:277px;background:var(--white);box-shadow:0 2px 8px rgba(0,0,0,.14)}
.cat-thumb{height:217px}
.cat-name{height:60px;display:flex;align-items:center;justify-content:center;text-align:center;font-family:'Poppins',sans-serif;font-weight:500;font-size:12.5px;line-height:17px;text-transform:uppercase}

/* newsletter */
.newsletter{left:0;top:2593px;width:1200px;height:365px;background:linear-gradient(120deg,#d9e8f4 0%,#f5f1ea 30%,#c9dff0 50%,#f6e6d6 75%,#cde2f2 100%)}
.nl-title{left:0;top:2650px;width:1200px;text-align:center;font-size:21px}
.nl-sub{left:0;top:2690px;width:1200px;text-align:center;font-size:20px;color:var(--muted)}
.field{top:2754px;width:325px;height:64px;border:1px solid #7b7b86;background:var(--white);padding-left:22px;display:flex;align-items:center;font-size:16px;color:#333}
.nl-btn{left:529px;top:2859px;width:136px;height:40px;line-height:40px;text-align:center;font-size:16px}

/* footer */
.footer-brand{left:132px;top:3005px;flex-direction:column;width:210px;height:210px;justify-content:center}
.footer-brand .brand-dot{width:190px;height:190px;display:flex;align-items:center;justify-content:center}
.footer-brand .brand-name{font-size:19px}
.f-col h4{font-family:'Poppins',sans-serif;font-weight:600;font-size:15px;text-transform:uppercase;color:var(--ink)}
.recent{left:443px;top:3004px;width:150px}
.recent li{list-style:none;font-size:13px;line-height:17px;color:var(--ink);padding:12px 0;border-bottom:1px solid #bcbcc4}
.recent li:last-child{border-bottom:0}
.recent ul{margin-top:10px}
.menu{left:679px;top:3004px}
.menu li{list-style:none;font-size:13px;text-transform:uppercase;line-height:24px}
.menu ul{margin-top:12px}
.follow-col{left:896px;top:3004px;width:200px}
.follow-col p{font-size:13px;line-height:22px;color:var(--purple);margin-top:16px}
.copyright{left:0;top:3235px;width:1200px;height:40px;background:var(--purple-dark);color:#e8e2f4;font-size:12px;text-align:center;line-height:40px}
</style>
</head>
<body>

<header class="site-header abs">
  <div class="brand header-brand abs"><span class="brand-dot"></span><span class="brand-name">NoraB Designs</span></div>
  <div class="search abs"><span>SEARCH</span>
    <svg width="12" height="12" viewBox="0 0 12 12"><circle cx="5" cy="5" r="3.8" fill="none" stroke="#777" stroke-width="1.4"/><line x1="8" y1="8" x2="11" y2="11" stroke="#777" stroke-width="1.4"/></svg>
  </div>
  <div class="follow abs"><span>FOLLOW US</span><span class="nets">Facelink · Gleam+ · Pictora · ClipVantor · Chirpa</span></div>
  <nav class="main-nav abs">
    <a class="active">Home</a><a>Cutora &amp; Pressbug</a><a>Products I Use</a><a>About Me!</a><a>Contact</a>
  </nav>
</header>

<section>
  <div class="hero abs" role="img" aria-label="Photo of three handmade watercolour greeting cards with large die-cut lettering and paper flowers"></div>
  <div class="hero-shade abs"></div>
  <div class="hero-arrow abs" style="left:0"><svg width="12" height="16" viewBox="0 0 12 16"><path d="M9 2 L3 8 L9 14" fill="none" stroke="#fff" stroke-width="2"/></svg></div>
  <div class="hero-arrow abs" style="left:1164px"><svg width="12" height="16" viewBox="0 0 12 16"><path d="M3 2 L9 8 L3 14" fill="none" stroke="#fff" stroke-width="2"/></svg></div>
  <div class="hero-panel abs">
    <h1 class="hero-title">The Beauty of Autumn!</h1>
    <p class="hero-text">There is nothing better than the colours of the autumn. Teal, rust, and cream are on the agenda for CTU516&nbsp; challenge.</p>
  </div>
  <a class="btn hero-btn abs">Read Most Recent Post</a>
</section>

<section>
  <div class="wash abs" style="left:990px;top:700px;width:230px;height:170px;background:rgba(190,170,220,.35)"></div>
  <div class="wash abs" style="left:-40px;top:1180px;width:230px;height:160px;background:rgba(190,170,220,.35)"></div>
  <h2 class="heading popular-title abs">Popular Posts<div class="rule"></div></h2>
  <div class="post-list abs">
    <article class="post-card">
      <div class="post-thumb" role="img" aria-label="Card with cartoon woodland animals on a kraft patterned background" style="background:linear-gradient(160deg,#a99a80,#7e7262)"></div>
      <h3 class="post-title">Aren't We All Smore's Lovers?</h3>
      <p class="post-text">In today's challenge we were supposed to use orange, brown, rust and yellow.</p>
      <span class="btn post-btn">Read More</span>
    </article>
    <article class="post-card">
      <div class="post-thumb" role="img" aria-label="Birthday card with a monster holding a green balloon above grass" style="background:linear-gradient(180deg,#cfe4ef,#7d9bb8 60%,#4f8a3a)"></div>
      <h3 class="post-title">Colour Toss-Up #513</h3>
      <p class="post-text">This week challenge was to use three colors, green, lime and navy blue.</p>
      <span class="btn post-btn">Read More</span>
    </article>
    <article class="post-card">
      <div class="post-thumb" role="img" aria-label="Card with silhouetted birds on a wire over a blue inked sky" style="background:linear-gradient(180deg,#b58a5e,#8fb3d9 30%,#dbe6f0 70%,#a9794b)"></div>
      <h3 class="post-title">Bird's On Wire!</h3>
      <p class="post-text">We all just need to not only get, but to send cards to remind others that we are thinking of them.</p>
      <span class="btn post-btn">Read More</span>
    </article>
    <article class="post-card">
      <div class="post-thumb" role="img" aria-label="Congratulations card with gold circles and stars" style="background:linear-gradient(160deg,#e9e2c8,#b7ad95 70%,#7a705e)"></div>
      <h3 class="post-title">Colour Toss-Up Challenge</h3>
      <p class="post-text">This is my first Challenge! I have done them, but never posted them.</p>
      <span class="btn post-btn">Read More</span>
    </article>
  </div>
</section>

<section>
  <div class="about abs"></div>
  <div class="brand about-brand abs"><span class="brand-dot"><span class="brand-name">NoraB Designs</span></span></div>
  <div class="about-copy abs">
    <h2 class="heading">About Me</h2>
    <div class="rule"></div>
    <p>Well, NoraB is a mother of three grown children, a daughter and two sons a daughter-in-law, and a grandmother of two gorgeous little ones, both are very special to me. Plus, one more on it way! I am currently on sick leave from work, due to an automobile accident last year. One being a concussion, and mobility of my neck. I also live with several disorders, Crohn's, Gastroparesis, Arterial Septal Defect, just to name a few.</p>
    <span class="btn about-btn">Read More</span>
  </div>
</section>

<section>
  <h2 class="heading cat-title abs">Categories<div class="rule"></div></h2>
  <div class="cat-grid abs">
    <div class="cat-card"><div class="cat-thumb" role="img" aria-label="Birds on a wire card" style="background:linear-gradient(180deg,#b58a5e,#8fb3d9 35%,#dbe6f0 70%,#a9794b)"></div><div class="cat-name">Inkvale</div></div>
    <div class="cat-card"><div class="cat-thumb" role="img" aria-label="Chalkboard first day of school sign" style="background:linear-gradient(160deg,#2b2b2e,#3b3a40)"></div><div class="cat-name">Back to School</div></div>
    <div class="cat-card"><div class="cat-thumb" role="img" aria-label="Woodland animals card" style="background:linear-gradient(160deg,#a99a80,#7e7262)"></div><div class="cat-name">Aren't We All<br>Smore's Lovers?</div></div>
    <div class="cat-card"><div class="cat-thumb" role="img" aria-label="Autumn leaves card" style="background:linear-gradient(160deg,#f3ede4,#c8865a 60%,#3d78a6)"></div><div class="cat-name">The Beauty of Autumn!</div></div>
    <div class="cat-card"><div class="cat-thumb" role="img" aria-label="Gold congratulations card" style="background:linear-gradient(160deg,#e9e2c8,#b7ad95 70%,#7a705e)"></div><div class="cat-name">Paper Crafting</div></div>
    <div class="cat-card"><div class="cat-thumb" role="img" aria-label="Flowers in a mason jar card with purple border" style="background:linear-gradient(180deg,#5a2f7a,#cfd8cd 20%,#b9cbbf 80%,#5a2f7a)"></div><div class="cat-name">Dievo</div></div>
    <div class="cat-card"><div class="cat-thumb" role="img" aria-label="Lace doily card with markers" style="background:linear-gradient(160deg,#d9cdb8,#b79f7e 60%,#6c6a6e)"></div><div class="cat-name">Hue Noire</div></div>
    <div class="cat-card"><div class="cat-thumb" role="img" aria-label="Runner wearing a red printed t-shirt outdoors" style="background:linear-gradient(180deg,#8fa7b8,#c93a3a 55%,#2e2a2a)"></div><div class="cat-name">T-Shirt</div></div>
  </div>
</section>

<section>
  <div class="newsletter abs"></div>
  <h2 class="heading nl-title abs">Newsletter Subscribe</h2>
  <p class="nl-sub abs">Get more details to signup</p>
  <div class="field abs" style="left:266px">Name</div>
  <div class="field abs" style="left:611px">Email id</div>
  <span class="btn nl-btn abs">Subscribe</span>
</section>

<footer>
  <div class="brand footer-brand abs"><span class="brand-dot"><span class="brand-name">NoraB Designs</span></span></div>
  <div class="f-col recent abs"><h4>Recent Posts</h4>
    <ul><li>Colour Toss-Up Challenge #507</li><li>Colour Toss-Up Challenge</li><li>The Beauty of Autumn!</li></ul>
  </div>
  <div class="f-col menu abs"><h4>Menu</h4>
    <ul><li>Home</li><li>Cutora &amp; Pressbug</li><li>Products I Use</li><li>About Me!</li><li>Contact</li></ul>
  </div>
  <div class="f-col follow-col abs"><h4>Follow Us</h4>
    <p>Facelink · Gleam+ · Pictora<br>ClipVantor · Chirpa</p>
  </div>
  <div class="copyright abs">Copyright © 2021 All Rights Reserved</div>
</footer>

</body>
</html>
```